Fast Business Card Project

I need a business card with the name RENATO DUARTE stylized on one side and my email on the other (renatocosta4711@mailnova.com)

Industry/Entity Type

Business

Contact Information for Business Card

www.trilhamar.com.br

```html
<!DOCTYPE html>
<html lang="pt-BR">
<head>
<meta charset="UTF-8">
<title>Cartão de visita – Trilhamar</title>
<link rel="stylesheet" href="https://fonts.googleapis.com/css2?family=Exo+2:wght@200;300;400;700&display=swap">
<style>
  :root {
    --backdrop: #1b1b1b;
    --card: #0f0f10;
    --card-edge: #262628;
    --ink: #e9e9ea;
    --ink-soft: #c9c9cb;
  }
  * { margin: 0; padding: 0; box-sizing: border-box; }
  html, body {
    width: 1200px;
    height: 799px;
    overflow: hidden;
    background: var(--backdrop);
  }
  .sheet {
    width: 1200px;
    height: 799px;
    display: flex;
    align-items: center;
    justify-content: center;
    gap: 60px;
    font-family: "Exo 2", sans-serif;
    color: var(--ink);
  }
  .card {
    width: 500px;
    height: 290px;
    background: var(--card);
    border: 1px solid var(--card-edge);
    position: relative;
  }
  .card--contact .contact {
    position: absolute;
    left: 44px;
    top: 116px;
  }
  .contact__name {
    font-size: 21px;
    letter-spacing: 0.5px;
    line-height: 1.1;
  }
  .contact__first { font-weight: 700; }
  .contact__last { font-weight: 300; }
  .contact__email {
    font-size: 15px;
    font-weight: 300;
    color: var(--ink-soft);
    margin-top: 4px;
  }
  .contact__site {
    font-size: 19px;
    font-weight: 400;
    margin-top: 2px;
  }
  .card--brand {
    display: flex;
    align-items: center;
    justify-content: center;
    gap: 18px;
  }
  .brand__name {
    font-size: 30px;
    font-weight: 700;
    letter-spacing: 1px;
    color: var(--ink);
  }
  .brand__divider {
    width: 1px;
    height: 52px;
    background: var(--ink);
  }
  .brand__site {
    font-size: 26px;
    font-weight: 200;
    color: var(--ink);
  }
</style>
</head>
<body>
  <main class="sheet">
    <section class="card card--contact">
      <div class="contact">
        <p class="contact__name"><span class="contact__first">RENATO</span> <span class="contact__last">DUARTE</span></p>
        <p class="contact__email">renatocosta4711@mailnova.com</p>
        <p class="contact__site">trilhamar.com.br</p>
      </div>
    </section>
    <section class="card card--brand">
      <span class="brand__name">TRILHAMAR</span>
      <span class="brand__divider"></span>
      <span class="brand__site">trilhamar.com.br</span>
    </section>
  </main>
</body>
</html>
```